Diesel Fitting/Mechanical Company Needs a new Business Card

We would like a new business card that showcases our logo and business information.

Industry/Entity Type

Business

Contact Information for Business Card

314 Wendale Street
PO Box 7581 BRAYFIELD QLD 4793
Phone: 49312787 Fax: 49312688 Mobile: 0438915276 ABN: 63 519 087 342

Requirements
Must have
• The following email addresses:
• admin@tkservicing.com.au , sales@tkservicing.com.au , accounts@tkservicing.com.au , parts@tkservicing.com.au , office@tkservicing.com.au
• Also need to have the website: www.tkservicing.com.au

```html
<!DOCTYPE html>
<html lang="en">
<head>
<meta charset="utf-8">
<title>TK Servicing Business Card</title>
<link href="https://fonts.googleapis.com/css2?family=Questrial&display=swap" rel="stylesheet">
<style>
  :root {
    --bg: #2a2a2a;
    --card: #ffffff;
    --ink: #1a1a1a;
    --orange: #f47a20;
    --yellow: #f6b81a;
    --red: #e1232a;
    --black: #111111;
    --dots: #333333;
  }
  * { margin: 0; padding: 0; box-sizing: border-box; }
  html, body { width: 1200px; height: 880px; overflow: hidden; }
  body {
    background: var(--bg);
    font-family: "Questrial", "Century Gothic", sans-serif;
    color: var(--ink);
    position: relative;
  }
  .card {
    position: absolute;
    width: 620px;
    height: 378px;
    background: var(--card);
    border-radius: 22px;
    overflow: hidden;
    box-shadow: 0 10px 30px rgba(0,0,0,0.45);
  }
  /* Back side */
  .card-back { left: 60px; top: 52px; }
  .note-title {
    position: absolute; top: 34px; width: 100%;
    text-align: center; font-size: 20px; font-weight: 400; letter-spacing: 1px;
  }
  .note-lines { position: absolute; left: 70px; top: 92px; width: 480px; }
  .note-line { height: 38px; border-bottom: 2px dotted var(--dots); }
  .accent-stripe {
    position: absolute; left: 0; right: 0; bottom: 42px; height: 5px;
    background: linear-gradient(90deg, var(--orange) 0%, var(--yellow) 50%, var(--red) 100%);
  }
  .footer-band {
    position: absolute; left: 0; right: 0; bottom: 0; height: 42px;
    background: var(--black); color: #fff;
    display: flex; align-items: center; justify-content: center;
    font-size: 16px; letter-spacing: 0.5px;
  }
  .footer-band .domain { color: var(--orange); }

  /* Front side */
  .card-front { left: 520px; top: 450px; }
  .brand {
    position: absolute; right: 32px; top: 32px;
    display: flex; align-items: center; gap: 12px;
  }
  .brand-dot { width: 34px; height: 34px; border-radius: 50%; background: var(--orange); }
  .brand-name { font-size: 32px; color: var(--ink); }
  .contact {
    position: absolute; left: 32px; top: 72px;
    font-size: 15px; line-height: 20px;
  }
  .address { margin-bottom: 10px; }
  .label { color: var(--orange); }
  .numbers { margin-bottom: 8px; }
  .email-heading { color: var(--orange); margin-bottom: 4px; }
  .email-row .sep { margin: 0 6px; }
  .wave { position: absolute; left: 0; top: 0; width: 620px; height: 378px; }
</style>
</head>
<body>

  <section class="card card-back" aria-label="Card back">
    <h2 class="note-title">NOTE</h2>
    <div class="note-lines">
      <div class="note-line"></div>
      <div class="note-line"></div>
      <div class="note-line"></div>
      <div class="note-line"></div>
      <div class="note-line"></div>
      <div class="note-line"></div>
    </div>
    <div class="accent-stripe"></div>
    <div class="footer-band">www.<span class="domain">tkservicing</span>.com.au</div>
  </section>

  <section class="card card-front" aria-label="Card front">
    <svg class="wave" viewBox="0 0 620 378" aria-hidden="true">
      <path d="M0,348 C240,344 440,328 620,282" fill="none" stroke="#f47a20" stroke-width="4"/>
      <path d="M0,358 C240,354 440,340 620,296 L620,378 L0,378 Z" fill="#111111"/>
    </svg>

    <div class="brand">
      <span class="brand-dot"></span>
      <span class="brand-name">TK Servicing</span>
    </div>

    <div class="contact">
      <p class="address">314 Wendale Street<br>PO Box 7581 BRAYFIELD<br>QLD 4793</p>
      <p class="numbers">
        <span class="label">Phone:</span> 49312787<br>
        <span class="label">Fax:</span> 49312688<br>
        <span class="label">Mobile:</span> 0438915276<br>
        <span class="label">ABN:</span> 63 519 087 342
      </p>
      <p class="email-heading">following email addresses:</p>
      <p class="email-row"><span class="label">E:</span> admin@tkservicing.com.au<span class="sep">|</span><span class="label">E:</span> sales@tkservicing.com.au</p>
      <p class="email-row"><span class="label">E:</span> accounts@tkservicing.com.au<span class="sep">|</span><span class="label">E:</span> parts@tkservicing.com.au</p>
      <p class="email-row"><span class="label">E:</span> office@tkservicing.com.au</p>
    </div>
  </section>

</body>
</html>
```